Business Card Design

Please visit www.MarkDorsey.com to acquire information for business card.

Back Side of Card:
a lifetime of experience working for you.

With over 25 years in the construction industry, well over a decade as a licensed Subcontractor / General Contractor and nearly 10 years as a licensed Realtor, I have excelled and cultivated a working knowledge of how all the pieces fit together.

Here is a link to folder.
https://files.examplecloud.net/folderview?id=7Qk2mXrTpLw9zVbN4sHcDyUeFaGj&usp=sharing

Industry/Entity Type

Construction

Contact Information for Business Card

Company: Mark Dorsey, LLC.
Address: 31872 W. Cedar Hollow Blvd. Suite 207-418
Name: Mark Dorsey
Phone: (623) 587-2914
Web: www.MarkDorsey.com
Type of services offered: Architectural Design, 3D Models, Renderings & Animation - Construction Documents - Project Managment.

```html
<!DOCTYPE html>
<html lang="en">
<head>
<meta charset="utf-8">
<title>Mark Dorsey LLC — Business Card</title>
<link rel="stylesheet" href="https://fonts.googleapis.com/css2?family=Arimo:wght@400;700&display=swap">
<style>
  :root {
    --bg: #e9e7ea;
    --orange: #f29219;
    --black: #0b0b0b;
    --card-w: 560px;
    --card-h: 320px;
  }
  * { box-sizing: border-box; margin: 0; padding: 0; }
  html, body { width: 1200px; height: 933px; overflow: hidden; }
  body {
    background: var(--bg);
    font-family: "Arimo", Arial, sans-serif;
    font-weight: 700;
    display: flex;
    flex-direction: column;
    align-items: center;
    justify-content: center;
    gap: 56px;
  }
  .card {
    position: relative;
    width: var(--card-w);
    height: var(--card-h);
    overflow: hidden;
    box-shadow: 0 8px 22px rgba(0,0,0,.18);
  }

  /* Front */
  .front { background: var(--orange); }
  .quad { position: absolute; width: 50%; height: 50%; }
  .quad--tl { left: 0; top: 0; background: var(--black); }
  .quad--tr { right: 0; top: 0; background: var(--orange); }
  .quad--bl { left: 0; bottom: 0; background: var(--orange); }
  .quad--br { right: 0; bottom: 0; background: var(--black); }
  .front-name {
    position: absolute;
    left: calc(50% + 18px);
    bottom: calc(50% + 16px);
    color: var(--black);
    font-size: 26px;
    line-height: 1;
    white-space: nowrap;
  }

  /* Back */
  .back { background: var(--orange); }
  .back-spine {
    position: absolute; left: 0; top: 0;
    width: 66px; height: 100%;
    background: var(--black);
  }
  .back-spine__name {
    position: absolute;
    left: 50%; top: 50%;
    transform: translate(-50%, -50%) rotate(-90deg);
    white-space: nowrap;
    color: var(--orange);
    font-size: 24px;
  }
  .contact {
    position: absolute;
    left: 88px; top: 26px;
    list-style: none;
    color: var(--black);
    font-size: 12px;
    line-height: 1;
  }
  .contact li + li { margin-top: 28px; }
  .contact__suite { display: block; margin: 6px 0 0 150px; }
  .name-tag {
    position: absolute;
    right: 0; top: 108px;
    background: var(--black);
    color: var(--orange);
    font-size: 22px;
    padding: 8px 14px 8px 18px;
  }
  .services {
    position: absolute;
    left: 66px; right: 0; bottom: 0;
    height: 104px;
    background: var(--black);
    color: var(--orange);
    font-size: 12.5px;
    line-height: 1.45;
    padding: 22px 28px 0 40px;
  }
</style>
</head>
<body>
  <section class="card front" aria-label="Business card front">
    <div class="quad quad--tl"></div>
    <div class="quad quad--tr"></div>
    <div class="quad quad--bl"></div>
    <div class="quad quad--br"></div>
    <span class="front-name">Mark Dorsey LLC</span>
  </section>

  <section class="card back" aria-label="Business card back">
    <div class="back-spine"><span class="back-spine__name">Mark Dorsey LLC</span></div>
    <ul class="contact">
      <li>PH: (623) 587-2914</li>
      <li>Web: www.MarkDorsey.com</li>
      <li>Address: 31872 W. Cedar Hollow Blvd.<span class="contact__suite">Suite 207-418</span></li>
    </ul>
    <div class="name-tag">Mark Dorsey</div>
    <p class="services">Services offered: Architectural Design, 3D Models, Renderings &amp; Animation - Construction Documents - Project Managment.</p>
  </section>
</body>
</html>
```